Real Estate 2015 sold listings postcard

Real estate. I want one side to list 2015 sales. Mailing side with additional information. I am including a "concept" but it needs to be professionalized... Feel free to change color, fonts, layout, add watermark, whatever you think will work. Text on backside may be tweaked. I do want postcards addressed. How do i send mailing list or does Brightmark Press do that part?

NOTE: Postcard should be 8.5 x 5.5 inches.
Updates

postcard should be 8.5" x 5.5" size

Target Market(s)

Home owners who may want to sell

Industry/Entity Type

Real Estate Agent

Requirements
Must have
• The sold information and contact oinformation I have provided
Nice to have
• Watermark with my initials

```html
<!DOCTYPE html>
<html lang="en">
<head>
<meta charset="utf-8">
<title>2015 Sales in Your Neighborhood</title>
<link href="https://fonts.googleapis.com/css2?family=Lato:wght@300;400;700;900&display=swap" rel="stylesheet">
<style>
:root{
  --red:#e02f36;
  --red-deep:#b8202a;
  --red-dark:#a51f27;
  --gold:#d4a20b;
  --gold-text:#d4a20b;
  --grey-band:#cfcfcf;
  --row-alt:#efefef;
  --ink:#333;
  --white:#fff;
}
*{margin:0;padding:0;box-sizing:border-box}
html,body{width:1200px;height:777px;overflow:hidden;background:#fff}
body{font-family:'Lato',sans-serif;color:var(--ink)}
.postcard{position:relative;width:1200px;height:777px;overflow:hidden;background:var(--white)}
.backdrop{position:absolute;inset:0}
.headline{position:absolute;right:34px;top:18px;text-align:right;color:var(--white);line-height:1}
.headline .year{font-size:56px;font-weight:300}
.headline .year b{font-weight:900}
.headline .sub{font-size:45px;font-weight:300;margin-top:10px;letter-spacing:.5px}
.headline .sub b{font-weight:900}
.sold-tab{position:absolute;left:978px;top:152px;width:154px;height:42px;background:var(--white);border-radius:22px 22px 0 0;
  color:var(--red-deep);font-weight:900;font-size:27px;text-align:center;line-height:44px}
.brand{position:absolute;left:28px;top:248px;width:276px;height:40px;display:flex;align-items:center;justify-content:center;gap:8px;white-space:nowrap}
.brand .mark{flex:none;width:14px;height:14px;background:var(--gold)}
.brand .name{font-size:24px;font-weight:900;color:#222;letter-spacing:.3px;line-height:1}
.portrait{position:absolute;left:88px;top:306px;width:156px;height:156px;border-radius:50%;
  background:radial-gradient(circle at 50% 45%,#c98f78 0%,#a2524a 45%,#2b2b2b 100%)}
.agent{position:absolute;left:28px;width:276px;text-align:center}
.agent-name{top:480px;font-size:28px;font-weight:700;color:var(--red-deep)}
.agent-role{top:518px;font-size:19px;color:var(--gold-text)}
.license{top:580px;font-size:20px;font-weight:300;color:#444;line-height:26px}
.web{position:absolute;left:28px;top:636px;width:276px;height:37px;background:var(--red-dark);color:var(--white);
  font-size:24px;font-weight:700;text-align:center;line-height:37px;white-space:nowrap}
.contact{position:absolute;left:28px;top:675px;width:276px;height:102px;background:var(--red);color:var(--white);text-align:center}
.contact .phone{font-size:38px;font-weight:300;margin-top:10px}
.contact .email{font-size:22px;margin-top:2px}
.sales{position:absolute;left:328px;top:192px;width:844px;border-collapse:collapse;table-layout:fixed;
  border:1px solid #9a9a9a;font-size:18px;background:var(--white)}
.sales th{background:var(--gold);color:var(--white);font-weight:400;height:31px;border-left:1px solid #e8c458}
.sales th:first-child{border-left:none}
.sales td{height:31.6px;padding:0 8px;white-space:nowrap}
.sales tbody tr:nth-child(even){background:var(--row-alt)}
.sales .c{text-align:center}
.sales .r{text-align:right}
.footnote{position:absolute;left:343px;top:743px;font-size:16.5px;color:#333;white-space:nowrap}
</style>
</head>
<body>
<div class="postcard">
  <svg class="backdrop" width="1200" height="777" viewBox="0 0 1200 777">
    <path d="M0 0H1200V265C1100 240 900 200 650 185C420 172 200 126 0 150Z" fill="var(--red)"/>
    <path d="M0 0H520C380 10 160 50 0 110Z" fill="var(--red-deep)" opacity=".55"/>
    <path d="M0 150C200 126 420 172 650 185C900 200 1100 240 1200 265V285C1100 262 900 222 650 207C420 194 200 160 0 196Z" fill="var(--gold)"/>
    <path d="M0 196C200 160 420 194 650 207C900 222 1100 262 1200 285V293C1100 272 900 232 650 216C420 204 200 172 0 206Z" fill="var(--grey-band)"/>
  </svg>

  <div class="headline">
    <div class="year"><b>2015</b> SALES</div>
    <div class="sub">IN YOUR <b>NEIGHBORHOOD</b></div>
  </div>

  <div class="brand"><span class="mark"></span><span class="name">COASTLINE REALTY</span></div>
  <div class="portrait" role="img" aria-label="Portrait photo of the agent"></div>
  <div class="agent agent-name">DIANE HOLLIS</div>
  <div class="agent agent-role">RELOCATION SPECIALIST</div>
  <div class="agent license">California License<br>#00482917</div>
  <div class="web">www.dhollishomes.com</div>
  <div class="contact">
    <div class="phone">650-555-0148</div>
    <div class="email">dhollis@coastline.com</div>
  </div>

  <div class="sold-tab">SOLD</div>
  <table class="sales">
    <colgroup><col style="width:180px"><col style="width:44px"><col style="width:72px"><col style="width:68px"><col style="width:92px"><col style="width:116px"><col style="width:128px"><col style="width:76px"><col style="width:68px"></colgroup>
    <thead><tr><th>Address</th><th>BR</th><th>BA</th><th>Sq Ft</th><th>Lot Size</th><th>List Price</th><th>Sale Price</th><th>$/Sq. Ft</th><th>DOM</th></tr></thead>
    <tbody>
      <tr><td>412 Alder PL*</td><td class="c">3</td><td class="c">3 1/2</td><td class="c">2588</td><td class="r">9239</td><td class="r">3,088,000</td><td class="r">3,100,000</td><td class="c">1,198</td><td class="r">9</td></tr>
      <tr><td>3580 Hawthorn ST</td><td class="c">4</td><td class="c">3</td><td class="c">2228</td><td class="r">6147</td><td class="r">2,998,000</td><td class="r">3,000,000</td><td class="c">1,346</td><td class="r">23</td></tr>
      <tr><td>218 Brookview DR</td><td class="c">4</td><td class="c">3</td><td class="c">2185</td><td class="r">7040</td><td class="r">2,500,000</td><td class="r">2,925,000</td><td class="c">1,339</td><td class="r">9</td></tr>
      <tr><td>455 Linden AVE*</td><td class="c">4</td><td class="c">2</td><td class="c">1611</td><td class="r">13,237</td><td class="r">2,498,000</td><td class="r">2,610,000</td><td class="c">1,620</td><td class="r">8</td></tr>
      <tr><td>4016 Maple AVE*</td><td class="c">4</td><td class="c">2</td><td class="c">2227</td><td class="r">8700</td><td class="r">2,295,000</td><td class="r">2,595,000</td><td class="c">1,165</td><td class="r">8</td></tr>
      <tr><td>74 Whitman CIR *</td><td class="c">3</td><td class="c">2</td><td class="c">1364</td><td class="r">5917</td><td class="r">1,788,000</td><td class="r">2,525,000</td><td class="c">1,851</td><td class="r">8</td></tr>
      <tr><td>3621 Sequoia CIR</td><td class="c">4</td><td class="c">2</td><td class="c">1646</td><td class="r">6404</td><td class="r">2,500,000</td><td class="r">2,475,000</td><td class="c">1,504</td><td class="r">18</td></tr>
      <tr><td>436 Canyon PL *</td><td class="c">3</td><td class="c">2</td><td class="c">1674</td><td class="r">11,200</td><td class="r">2,498,000</td><td class="r">2,450,000</td><td class="c">1,464</td><td class="r">16</td></tr>
      <tr><td>273 Brookview DR*</td><td class="c">4</td><td class="c">2</td><td class="c">1690</td><td class="r">8178</td><td class="r">2,199,000</td><td class="r">2,400,000</td><td class="c">1,420</td><td class="r">7</td></tr>
      <tr><td>309 Brookview DR.</td><td class="c">3</td><td class="c">2</td><td class="c">1674</td><td class="r">8538</td><td class="r">2,200,000</td><td class="r">2,260,000</td><td class="c">1,350</td><td class="r">97</td></tr>
      <tr><td>91 Whitman CIR</td><td class="c">3</td><td class="c">2</td><td class="c">1243</td><td class="r">6080</td><td class="r">1,488,000</td><td class="r">2,250,000</td><td class="c">1,810</td><td class="r">7</td></tr>
      <tr><td>3718 Larkin CIR *</td><td class="c">4</td><td class="c">2</td><td class="c">1333</td><td class="r">6493</td><td class="r">1,895,000</td><td class="r">2,227,500</td><td class="c">1,671</td><td class="r">6</td></tr>
      <tr><td>358 Meadow DR *</td><td class="c">3</td><td class="c">2</td><td class="c">1740</td><td class="r">6324</td><td class="r">2,200,000</td><td class="r">2,180,000</td><td class="c">1,253</td><td class="r">12</td></tr>
      <tr><td>3642 Hawthorn ST</td><td class="c">4</td><td class="c">2</td><td class="c">1474</td><td class="r">6111</td><td class="r">1,799,900</td><td class="r">2,115,000</td><td class="c">1,435</td><td class="r">17</td></tr>
      <tr><td>62 Whitman Cir</td><td class="c">4</td><td class="c">2</td><td class="c">1456</td><td class="r">6111</td><td class="r">1,788,000</td><td class="r">2,000,000</td><td class="c">1,374</td><td class="r">11</td></tr>
      <tr><td>247 Glenwood CT</td><td class="c">3</td><td class="c">2</td><td class="c">1428</td><td class="r">10,624</td><td class="r">1,950,000</td><td class="r">2,100,000</td><td class="c">1,471</td><td class="r">20</td></tr>
    </tbody>
  </table>
  <div class="footnote">* indicates Coastline Realty listing or sale. This information is deemed reliable, but not verified or guaranteed.</div>
</div>
</body>
</html>
```